Chiropractic office needs updated web site

take the information/content from my existing website and redesign it to be more efficient and modern looking. i have a logo already designed that i have provided the files for. my office sees primarily athletes and their families and is geared toward active, healthy people who have sports injuries.
Updates

i originally started the project in february 2019 but am now just able to post the project. i need a new deadline calculated from todays (6-9-19) date.

Target Market(s)

injured athletes looking for a specific type of chiropractor.

Industry/Entity Type

Health Care

Contact Information for Business Card

I have a logo already designed and will provide that to all designers!

Coding

Coded - Design and coding required

Number of Pages Required

1 page

Font styles to use
Sans Serif

Colors

Designer to choose colors to be used in the design.

Requirements
Must have
• the current information/content already contained in my current website, belvanspinefit.com. i want this info redesigned and/or transferred to a new template. i will also provide new updated photos for use on the new site!
Nice to have
• modern, minimalist, creative looking website
Should not have
• typical medical website with boring, over-used stock photos of doctors, nurses and generic family types

```html
<!DOCTYPE html>
<html lang="en">
<head>
<meta charset="utf-8">
<title>Belvan Chiropractic and Sports Therapy</title>
<link href="https://fonts.googleapis.com/css2?family=Oswald:wght@300;400;500;600;700&family=PT+Sans+Narrow:wght@400;700&display=swap" rel="stylesheet">
<style>
:root{
  --cyan:#0fb9ec;
  --cyan-soft:rgba(64,205,240,.88);
  --red:#e8141c;
  --black:#000;
  --charcoal:#111;
  --footer:#2a2a2a;
  --footer-bottom:#f3f3f3;
  --white:#fff;
  --grey-text:#cfcfcf;
  --dark-text:#333;
}
*{margin:0;padding:0;box-sizing:border-box}
html,body{width:1200px;height:3945px;overflow:hidden}
body{font-family:"PT Sans Narrow",sans-serif;background:var(--white);position:relative;color:var(--white)}
.abs{position:absolute}
h1,h2,h3,.brand,.nav a,.btn{font-family:"Oswald",sans-serif}

/* header */
.topbar{top:0;left:0;width:1200px;height:122px;background:var(--white)}
.contact-chip{display:flex;align-items:center;gap:10px;color:var(--dark-text)}
.chip-icon{width:48px;height:48px;border-radius:50%;background:#f1f1f1;display:flex;align-items:center;justify-content:center}
.chip-label{font-family:"Oswald",sans-serif;color:var(--cyan);font-size:14px}
.chip-value{font-size:12px}
.brand{display:flex;align-items:center;gap:10px;color:var(--cyan);font-weight:500;letter-spacing:3px}
.brand-dot{width:44px;height:44px;border-radius:50%;background:var(--cyan)}
.brand-name{font-size:26px;line-height:1}
.brand-sub{font-size:10px;letter-spacing:5px;color:#666;font-weight:300}

.nav{top:122px;left:0;width:1200px;height:51px;background:var(--cyan)}
.nav a{position:absolute;top:0;height:51px;line-height:51px;color:var(--white);font-size:14px;font-weight:300;text-decoration:none}
.nav a.active{background:var(--red);padding:0 18px}

/* hero */
.hero{top:173px;left:0;width:1200px;height:569px;background:linear-gradient(100deg,#d9ddd6 0%,#eeeeec 35%,#e4dcd4 65%,#cfc8c0 100%)}
.hero-title{top:130px;left:0;width:1200px;text-align:center;font-size:60px;line-height:64px;font-weight:700;letter-spacing:3px;color:var(--white)}
.hero-sub{top:290px;left:0;width:1200px;text-align:center;font-size:12px;color:var(--white)}
.btn{display:block;text-align:center;color:var(--white);background:var(--red);border-radius:24px;font-size:14px;font-weight:300;text-decoration:none}
.dots{top:500px;left:582px;display:flex;gap:8px}
.dots span{width:10px;height:10px;border-radius:50%;background:rgba(255,255,255,.7)}
.dots span.on{background:var(--cyan)}

/* mission */
.mission{top:742px;left:0;width:1200px;height:480px;background:var(--black)}
.photo{background:linear-gradient(135deg,#8a8a8a,#d8d8d8)}
.section-h{font-size:32px;font-weight:500}
.section-h .accent{color:var(--cyan)}
.rule{height:4px;background:var(--cyan)}
.body-copy{font-size:12px;line-height:29px;color:var(--white)}

/* treatments */
.treatments{top:1222px;left:0;width:1200px;height:523px;background:var(--charcoal)}
.center-h{left:0;width:1200px;text-align:center;font-size:32px;font-weight:500}
.card{top:162px;width:290px;height:297px;border-radius:16px;overflow:hidden}
.card-label{position:absolute;left:0;bottom:0;width:100%;height:61px;line-height:61px;text-align:center;background:var(--cyan-soft);font-family:"Oswald",sans-serif;font-size:19px}
.arrow{top:280px;width:48px;height:48px;border-radius:50%;background:var(--white);border:2px solid var(--cyan);display:flex;align-items:center;justify-content:center}

/* doctors */
.doctors{top:1745px;left:0;width:1200px;height:1069px;background:var(--black)}
.doc-name{font-size:32px;font-weight:500}
.read-more{font-family:"Oswald",sans-serif;font-size:12px;color:var(--cyan);text-decoration:underline}

/* gallery */
.gallery{top:2814px;left:0;width:1200px;height:769px;background:var(--charcoal)}
.grid{top:168px;left:0;width:1200px;display:grid;grid-template-columns:repeat(4,300px);grid-auto-rows:230px}

/* footer */
.footer{top:3583px;left:0;width:1200px;height:306px;background:var(--footer)}
.foot-h{font-size:19px;font-weight:500}
.foot-item{display:flex;align-items:center;gap:18px;font-size:12px;line-height:20px}
.input{background:var(--white);border-radius:20px;color:#999;font-size:10px;padding-left:24px;line-height:38px}
.copyright{top:3889px;left:0;width:1200px;height:56px;background:var(--footer-bottom);color:#666;font-size:12px;text-align:center;line-height:56px}
</style>
</head>
<body>

<header class="abs topbar">
  <div class="abs contact-chip" style="left:221px;top:37px">
    <div class="chip-icon">
      <svg width="18" height="18" viewBox="0 0 24 24"><path d="M6.6 10.8a15 15 0 0 0 6.6 6.6l2.2-2.2c.3-.3.7-.4 1-.2 1.1.4 2.3.6 3.6.6.6 0 1 .4 1 1V20c0 .6-.4 1-1 1C10.6 21 3 13.4 3 4c0-.6.4-1 1-1h3.5c.6 0 1 .4 1 1 0 1.2.2 2.4.6 3.6.1.3 0 .7-.2 1z" fill="#0fb9ec"/></svg>
    </div>
    <div><div class="chip-label">Need any help?</div><div class="chip-value">+123-456-7890</div></div>
  </div>
  <div class="abs brand" style="left:470px;top:36px">
    <div class="brand-dot"></div>
    <div><div class="brand-name">BELVAN</div><div class="brand-sub">CHIROPRACTIC AND SPORTS THERAPY</div></div>
  </div>
  <div class="abs contact-chip" style="left:815px;top:37px">
    <div class="chip-icon">
      <svg width="18" height="14" viewBox="0 0 20 14"><rect x="1" y="1" width="18" height="12" fill="#0fb9ec"/><path d="M1 1l9 7 9-7" stroke="#fff" stroke-width="1.5" fill="none"/></svg>
    </div>
    <div><div class="chip-label">Email Us!</div><div class="chip-value">info@belvanspinefit.com</div></div>
  </div>
</header>

<nav class="abs nav">
  <a class="active" href="#" style="left:155px">Home</a>
  <a href="#" style="left:250px">Location</a>
  <a href="#" style="left:336px">Treatments Offered</a>
  <a href="#" style="left:476px">New Patient Paperwork</a>
  <a href="#" style="left:637px">Stretching</a>
  <a href="#" style="left:733px">Gallery</a>
  <a href="#" style="left:812px">Contact Us</a>
  <svg class="abs" style="left:975px;top:18px" width="16" height="16" viewBox="0 0 16 16"><circle cx="6.5" cy="6.5" r="5" stroke="#fff" stroke-width="1.5" fill="none"/><path d="M10.5 10.5L15 15" stroke="#fff" stroke-width="1.5"/></svg>
</nav>

<section class="abs hero" role="img" aria-label="Therapist stretching the arm of a woman lying on a treatment table in a bright room">
  <h1 class="abs hero-title">THE BEST THERAPY AND<br>INJURIES TREATMENT</h1>
  <p class="abs hero-sub">At Belvan Chiropractic, you can get professional treatment of a wide range of injuries and experience advanced therapy</p>
  <a class="abs btn" href="#" style="left:528px;top:351px;width:142px;height:44px;line-height:44px">Get In Touch</a>
  <div class="abs dots"><span></span><span class="on"></span><span></span></div>
</section>

<section class="abs mission">
  <div class="abs photo" role="img" aria-label="Athletes training with a coach in a clinic" style="left:155px;top:53px;width:274px;height:261px;background:linear-gradient(135deg,#cfd6d8,#6f7b72)"></div>
  <div class="abs photo" role="img" aria-label="Doctor examining an athlete's knee" style="left:335px;top:152px;width:274px;height:262px;background:linear-gradient(135deg,#e3e3e3,#5a5a5a)"></div>
  <h2 class="abs section-h" style="left:649px;top:114px">Mission <span class="accent">Statement</span></h2>
  <div class="abs rule" style="left:649px;top:166px;width:88px;height:3px"></div>
  <p class="abs body-copy" style="left:649px;top:198px;width:400px">Our goal at Belvan Chiropractic and Sports Therapy is to facilitate healing and optimum physical performance through a partnership with our patients. By restoring balance to the body – muscle, joint and nerve – we provide a starting point where the patient can then take control of their health and well-being. The doctors here provide assessment and instruction on proper posture, exercise biomechanics, nutrition and lifestyle behaviors needed to maintain the health benefits achieved here in our office.</p>
</section>

<section class="abs treatments">
  <h2 class="abs center-h" style="top:40px">Treatments Offered</h2>
  <div class="abs rule" style="left:533px;top:104px;width:132px"></div>
  <div class="abs card" role="img" aria-label="Therapist working on a woman's shoulder" style="left:139px;background:linear-gradient(160deg,#f4f1ee,#c9b8aa)"><div class="card-label">The Belvan Protocol</div></div>
  <div class="abs card" role="img" aria-label="Resistance band stretch on a leg" style="left:453px;background:linear-gradient(160deg,#e8ddd2,#a98b74)"><div class="card-label">Myofascial Release</div></div>
  <div class="abs card" role="img" aria-label="Runner holding her knee on a forest trail" style="left:769px;background:linear-gradient(160deg,#7aa05a,#3d5a2c)"><div class="card-label">Active Release Therapy</div></div>
  <div class="abs arrow" style="left:115px"><svg width="12" height="14" viewBox="0 0 12 14"><path d="M8 2L3 7l5 5" stroke="#0fb9ec" stroke-width="2" fill="none"/></svg></div>
  <div class="abs arrow" style="left:1034px"><svg width="12" height="14" viewBox="0 0 12 14"><path d="M4 2l5 5-5 5" stroke="#0fb9ec" stroke-width="2" fill="none"/></svg></div>
</section>

<section class="abs doctors">
  <div class="abs photo" role="img" aria-label="Portrait of Dr. Reed Belvan" style="left:139px;top:71px;width:369px;height:447px;background:linear-gradient(160deg,#5a4a40,#b0a4c4)"></div>
  <h3 class="abs doc-name" style="left:536px;top:88px">Dr. Reed Belvan</h3>
  <p class="abs body-copy" style="left:536px;top:150px;width:520px">Dr. Reed Belvan is the owner and clinic director for Belvan Chiropractic and Sports Therapy. He is a native Texan, growing up in the Dallas area and attended Lakeside State University on a basketball scholarship. Upon finishing his academic and basketball career at LSU-T, Dr. Belvan traveled and worked throughout Europe for 3 years before discovering beach volleyball and relocating to Miami Beach, FL. It was while competing on the East Coast pro-beach volleyball circuit that he experienced the awesome power of chiropractic and physical medicine. The injuries and chronic conditions that are a part of playing competitive sports had become debilitating for Dr. Belvan at a time when he should have been at peak physical condition and performance. Through a combination of chiropractic treatment, physical medicine and soft-tissue therapy, Dr. Belvan was able to resume playing the sport he loved pain free and stronger than ever. It was this experience that ultimately led him to return to school to pursue his chiropractic degree with the desire to bring this life-changing healing experience to other athletes and all those suffering from similar conditions. Although the "spark had been lit" from these experiences, Dr. Belvan felt the time was not right and he continued traveling and playing beach volleyball.</p>
  <a class="abs read-more" href="#" style="left:536px;top:485px">Read More</a>

  <h3 class="abs doc-name" style="left:145px;top:593px">Dr. Lena Hartwell</h3>
  <p class="abs body-copy" style="left:145px;top:655px;width:520px">Dr. Lena Hartwell attended chiropractic school at Ridgeway University in Dallas, TX, and is originally from Ardmore, OK. She started her career in healthcare there as a licensed massage therapist, but quickly decided that her clients needed more than what massage could offer. "How could I release muscle tissue but not address the joint dysfunction?" "What would be the best way to make profound, life-long changes in peoples' lives?", she asked herself. In her quest to answer these questions, Dr. Hartwell found chiropractic and her true passion.<br><br>Since graduating from Ridgeway University, Dr. Hartwell has sought to integrate soft tissue therapy, chiropractic and multiple modalities into her professional philosophy, always seeking "new and better ways to get people better!" Upon meeting Dr. Belvan, she knew she had found her mentor and has continued to evolve and thrive under his tutelage. She states, "The Belvan Protocol, in my opinion, is the perfect marriage between soft tissue work and the treatment of joint function.</p>
  <a class="abs read-more" href="#" style="left:145px;top:963px">Read More</a>
  <div class="abs photo" role="img" aria-label="Portrait of Dr. Lena Hartwell" style="left:678px;top:559px;width:368px;height:447px;background:linear-gradient(160deg,#8a5a38,#c9b6a0)"></div>
</section>

<section class="abs gallery">
  <h2 class="abs center-h" style="top:48px">Our Gallery</h2>
  <div class="abs rule" style="left:533px;top:119px;width:132px"></div>
  <div class="abs grid">
    <div role="img" aria-label="Indoor volleyball match" style="background:linear-gradient(135deg,#3a4a6a,#b8a48c)"></div>
    <div role="img" aria-label="Football player running with the ball" style="background:linear-gradient(135deg,#c62a2a,#6a1a1a)"></div>
    <div role="img" aria-label="Softball batter at the plate" style="background:linear-gradient(135deg,#a04040,#c8c0b0)"></div>
    <div role="img" aria-label="Smiling athlete in a team shirt" style="background:linear-gradient(135deg,#7a7a7a,#c8beb0)"></div>
    <div role="img" aria-label="Signed beach volleyball photo" style="background:linear-gradient(135deg,#4a6e9a,#d0b89a)"></div>
    <div role="img" aria-label="Signed photo of a volleyball player diving" style="background:linear-gradient(135deg,#3a6a9a,#d8c090)"></div>
    <div role="img" aria-label="Group of friends at the beach" style="background:linear-gradient(135deg,#5a8ab0,#b08a6a)"></div>
    <div role="img" aria-label="Signed photo of a player diving in the sand" style="background:linear-gradient(135deg,#e8e4de,#c8b090)"></div>
  </div>
  <a class="abs btn" href="#" style="left:514px;top:681px;width:169px;height:48px;line-height:48px;border:1px solid #fff">View All</a>
</section>

<footer class="abs footer">
  <div class="abs brand" style="left:184px;top:52px">
    <div class="brand-dot"></div>
    <div><div class="brand-name">BELVAN</div><div class="brand-sub">CHIROPRACTIC AND SPORTS THERAPY</div></div>
  </div>
  <p class="abs" style="left:184px;top:126px;width:290px;font-size:14px;line-height:29px;color:var(--grey-text)">Sed ut perspiciatis unde omnis iste natus error sit voluptatem accusantium doloremque laudantium, totam rem aperiam,</p>
  <div class="abs" style="left:184px;top:236px;width:22px;height:22px;border:2px solid #666;border-radius:4px"></div>

  <h3 class="abs foot-h" style="left:540px;top:60px">Get&nbsp; In Touch</h3>
  <div class="abs foot-item" style="left:545px;top:123px">
    <svg width="18" height="18" viewBox="0 0 24 24"><path d="M6.6 10.8a15 15 0 0 0 6.6 6.6l2.2-2.2c.3-.3.7-.4 1-.2 1.1.4 2.3.6 3.6.6.6 0 1 .4 1 1V20c0 .6-.4 1-1 1C10.6 21 3 13.4 3 4c0-.6.4-1 1-1h3.5c.6 0 1 .4 1 1 0 1.2.2 2.4.6 3.6.1.3 0 .7-.2 1z" fill="none" stroke="#ccc" stroke-width="1.5"/></svg>
    <span>+123-456-7890</span>
  </div>
  <div class="abs foot-item" style="left:545px;top:169px">
    <svg width="18" height="14" viewBox="0 0 20 14"><rect x="1" y="1" width="18" height="12" fill="none" stroke="#ccc" stroke-width="1.5"/><path d="M1 1l9 7 9-7" stroke="#ccc" stroke-width="1.5" fill="none"/></svg>
    <span>hello@belvanspinefit.com</span>
  </div>
  <div class="abs foot-item" style="left:545px;top:210px">
    <svg width="18" height="20" viewBox="0 0 18 22"><path d="M9 21s7-7.5 7-12.5A7 7 0 0 0 2 8.5C2 13.5 9 21 9 21z" fill="none" stroke="#ccc" stroke-width="1.5"/><circle cx="9" cy="8.5" r="2.5" fill="none" stroke="#ccc" stroke-width="1.5"/></svg>
    <span>123 Lorem Ipsum is a<br>simple Dummy text</span>
  </div>

  <h3 class="abs foot-h" style="left:770px;top:60px">Newsletter</h3>
  <div class="abs input" style="left:775px;top:125px;width:235px;height:38px">Email Address...</div>
  <a class="abs btn" href="#" style="left:775px;top:183px;width:235px;height:37px;line-height:37px;font-weight:600">Subscribe</a>
</footer>

<div class="abs copyright">Copyright © 2019 Belvan Chiropractic</div>

</body>
</html>
```